Zielgruppe
Die Brandauer Lederwaren GmbH hat ihren Hauptsitz in Schwanstetten bei Nürnberg. Wir befassen uns mit der Produktion und dem
Vertrieb von Lederwaren und haben langjährige Erfahrung im nationalen sowie internationalen Tagesgeschäft. Zudem planen und
entwickeln wir kundenspezifische Artikel und arbeiten mit namhaften Partnern aus sämtlichen Branchen eng zusammen. Unser Personal
umfasst mehr als 30 Mitarbeiter aus den Bereichen Einkauf, Entwicklung, Logistik und Vertrieb.
Aufgabenstellung
Für unsere neue Produktgruppe "Sunny Days" soll ein Flyer entworfen werden, der unsere Kunden auf die bevorstehende Lieferfähigkeit der Produkte hinweist.
Damit der Flyer in Briefsendungen beigelegt werden kann sollte er ein Format von DIN Lang haben, also das Format eines Briefkuverts. Beschnittzugabe sollte auf jeder Seite 2 mm sein.
Die Artikel sind lieferbar ab September und können entsprechend von uns bezogen werden.
Unsere Schmuck- und Uhrenkästen werden unter einem Markennamen vertrieben, dies soll auch im Flyer zum Ausdruck kommen.
Eine entsprechende Logodatei sowie das entsprechende CI Manual ist im Bildpaket enthalten.
Die Gruppe besteht aus:
1 Schmuckkasten groß
1 Schmuckkasten klein
Als Hintergrund soll ein Thema gewählt werden, welches zum typischen "Sunny Days"-Umfeld passt, z.B. der Union Jack oder andere typisch britische Motive (sollte unklar sein, was es m it "Sunny Days" auf sich hat, so ist über google jede Menge Info darüber ausfindig zu machen).
Das Motiv der Schmuckkästen soll so gut wie möglich rüberkommen, deshalb sind im Bildpaket verschiedene Varianten und Aufnahmewinkel enthalten. Da auf den beiden Kästen unterschiedliche Motive abgebildet sind, sollen beide Kästen geschlossen und offen abgebildet sein.
Die CI-konforme Schriftart zur Erstellung der Produktbeschreibungen ist Italian Old Style (siehe Dateipaket). Auch die Schriftart und die ReadMe Datei für das zu erstellende Sunny Days Motiv sind beigefügt.
Die Artikelnummern, die Preisstellungen sowie die Beschreibungen sollen in Kurzform mit zu den Produkten gedruckt werden. Bei den Preisstellungen müssen sowohl der Händler-Einkaufspreis (ausgewiesen mit "Einkaufspreis" oder "Händler-EK") als auch die unverbindliche Preisempfehlung (angegeben mit "ÚPE") eingearbeitet sein. Alle Informationen sind in der Excel-Tabelle enthalten.
Weiterhin soll als Bestellmöglichkeit die folg..

```html
<!DOCTYPE html>
<html lang="de">
<head>
<meta charset="utf-8">
<title>Brandauer – Sunny Days Flyer</title>
<link rel="stylesheet" href="https://fonts.googleapis.com/css2?family=Montserrat:wght@700&family=Sorts+Mill+Goudy:ital@0;1&display=swap">
<style>
  :root{
    --page:#f3f3f3;
    --navy:#0f2438;
    --white:#ffffff;
    --blue:#1d4fbf;
    --violet:#6a3aa8;
    --magenta:#d62a6a;
    --lacquer:#e23a2e;
    --pink:#ec5aa8;
    --ink-soft:rgba(255,255,255,.92);
  }
  *{margin:0;padding:0;box-sizing:border-box}
  html,body{width:847px;height:1200px;overflow:hidden;background:var(--page)}
  .canvas{position:relative;width:847px;height:1200px}
  .flyer{position:absolute;top:222px;width:360px;height:756px;overflow:hidden;color:var(--white)}
  .flyer--front{left:38px;
    background:
      radial-gradient(circle at 30% 40%, rgba(106,58,168,.7), transparent 55%),
      linear-gradient(180deg,var(--magenta) 0%,var(--violet) 40%,#4a3fb0 70%,var(--blue) 100%)}
  .flyer--back{left:448px;
    background:
      radial-gradient(circle at 70% 30%, rgba(120,110,210,.55), transparent 45%),
      linear-gradient(180deg,var(--blue) 0%,#4f46b8 30%,#a0348e 55%,var(--magenta) 80%,#e0245a 100%)}

  /* front */
  .brand-plate{position:absolute;left:121px;top:43px;width:239px;height:77px;background:var(--navy);
    display:flex;align-items:center;justify-content:center;gap:10px}
  .brand-plate__mark{width:9px;height:9px;background:var(--white)}
  .brand-plate__name{font-family:"Sorts Mill Goudy",serif;font-size:24px;letter-spacing:1px;color:var(--white)}
  .motif-flag{position:absolute;left:0;top:140px;width:360px;height:260px;
    background:linear-gradient(135deg,rgba(232,40,58,.75),rgba(120,70,190,.5) 50%,rgba(232,40,58,.7));opacity:.85}
  .motif-crown{position:absolute;left:137px;top:192px;width:92px;height:90px;border-radius:8px;
    background:rgba(255,255,255,.85)}
  .motif-tower{position:absolute;left:270px;top:370px;width:84px;height:386px;
    background:linear-gradient(180deg,rgba(140,110,220,.35),rgba(80,90,210,.45))}
  .motif-portrait{position:absolute;left:0;top:330px;width:110px;height:260px;
    background:linear-gradient(180deg,rgba(70,50,150,.45),rgba(60,70,180,.35))}
  .headline{position:absolute;left:0;width:360px;text-align:center;display:block;
    font-family:"Montserrat",sans-serif;font-weight:700;line-height:1;color:var(--white);letter-spacing:-2px}
  .headline--l1{top:312px;font-size:74px}
  .headline--l2{top:394px;font-size:74px}
  .headline--and{top:482px;font-size:40px;letter-spacing:-1px}
  .headline--l3{top:526px;font-size:78px}
  .headline--l4{top:606px;font-size:82px}

  /* back */
  .serif{font-family:"Sorts Mill Goudy",serif}
  .line{position:absolute;white-space:nowrap;line-height:1}
  .line--small{font-size:13px;color:var(--ink-soft)}
  .line--title{font-size:15.5px}
  .line--price{font-size:34px}
  .line--price small{font-size:18px;margin-right:3px}
  .line--claim{font-size:25px;font-style:italic}
  .photo{position:absolute;background:linear-gradient(160deg,#f04a3a,var(--lacquer) 60%,#b8231d);border-radius:2px}
  .pattern-dahlia{position:absolute;left:178px;top:506px;width:182px;height:250px;
    background:radial-gradient(circle at 70% 60%,rgba(236,90,168,.7),rgba(236,90,168,0) 70%)}
</style>
</head>
<body>
<main class="canvas">

  <section class="flyer flyer--front" aria-label="Flyer Vorderseite">
    <div class="motif-flag" role="img" aria-label="Wehender Union Jack in Rot und Violett"></div>
    <div class="motif-portrait" role="img" aria-label="Schemenhafte Illustration einer britischen Wache"></div>
    <div class="motif-tower" role="img" aria-label="Silhouette des Big Ben"></div>
    <div class="brand-plate">
      <span class="brand-plate__mark"></span>
      <span class="brand-plate__name">Brandauer</span>
    </div>
    <div class="motif-crown" role="img" aria-label="Weiße Krone"></div>
    <h1>
      <span class="headline headline--l1">SUNNY</span>
      <span class="headline headline--l2">DAYS</span>
      <span class="headline headline--and">AND</span>
      <span class="headline headline--l3">WEAR</span>
      <span class="headline headline--l4">PEARLS</span>
    </h1>
  </section>

  <section class="flyer flyer--back serif" aria-label="Flyer Rückseite">
    <div class="pattern-dahlia" role="img" aria-label="Dekoratives Blütenmuster in Pink"></div>

    <div class="photo" style="left:194px;top:41px;width:166px;height:118px" role="img" aria-label="Großer roter Schmuckkasten geschlossen"></div>
    <div class="photo" style="left:8px;top:160px;width:133px;height:140px" role="img" aria-label="Großer roter Schmuckkasten geöffnet mit Spiegel"></div>
    <div class="photo" style="left:185px;top:307px;width:160px;height:120px" role="img" aria-label="Kleiner roter Schmuckkasten geschlossen"></div>
    <div class="photo" style="left:253px;top:408px;width:107px;height:128px" role="img" aria-label="Kleiner roter Schmuckkasten geöffnet mit Spiegel"></div>

    <p class="line line--small" style="left:34px;top:44px">Art.-Nr. 41207-5</p>
    <p class="line line--small" style="left:34px;top:64px">Einkaufspreis</p>
    <p class="line line--price" style="left:34px;top:86px"><small>€</small>82,90</p>
    <p class="line line--small" style="left:34px;top:122px">UPE: 199,00 €</p>

    <p class="line line--title" style="left:156px;top:183px">Schmuckkasten aus Echtholz</p>
    <p class="line line--small" style="left:156px;top:204px">mit Überzug in Klavierlackoptik</p>
    <p class="line line--small" style="left:156px;top:244px">Farbe: rot / beige</p>
    <p class="line line--small" style="left:156px;top:264px">ca. 30,5 x 21 x 16 cm</p>

    <p class="line line--small" style="left:34px;top:330px">Art.-Nr. 41208-5</p>
    <p class="line line--small" style="left:34px;top:350px">Einkaufspreis</p>
    <p class="line line--price" style="left:34px;top:372px"><small>€</small>70,40</p>
    <p class="line line--small" style="left:34px;top:410px">UPE: 169,00 €</p>

    <p class="line line--title" style="left:34px;top:454px">Schmuckkasten aus Echtholz</p>
    <p class="line line--small" style="left:34px;top:475px">mit Überzug in Klavierlackoptik</p>
    <p class="line line--small" style="left:34px;top:515px">Farbe: rot / beige</p>
    <p class="line line--small" style="left:34px;top:535px">ca. 25,5 x 16,5 x 13 cm</p>

    <p class="line line--claim" style="left:33px;top:597px">Luxus neu entdecken</p>
    <p class="line line--small" style="left:33px;top:634px">Brandauer Lederwaren GmbH</p>
    <p class="line line--small" style="left:33px;top:652px">Am Lindenhof 4, 73312 Lindenfeld</p>
    <p class="line line--small" style="left:33px;top:687px">T&nbsp; +49 7331 5530.0 &nbsp;&nbsp; F&nbsp; +49 7331 5530.94</p>
    <p class="line line--small" style="left:33px;top:705px">info@brandauer-lederwaren.de</p>
    <p class="line line--small" style="left:33px;top:723px">www.brandauer-lederwaren.de</p>
  </section>

</main>
</body>
</html>
```